Cards & Invitations

Hi!
We would like you to design 3 amazing cards for us.
1. Wedding invitation.
We would like to have a spring wedding invitation. It has to be A4 folded to A5 format, floral theme, but made in a very classic style. It has to contain light green and blue colors, but you are free to use other colors as well.
Text to be included:
Mr. and Mrs. Delwyn Avercross
Request the honour of your presence
At the marriage of their daughter
Marisse Avercross
to
Owen Ralditch
Saturday, the eighteenth of April
Two thousand and twelve
At three o'clock in the afternoon
Saint Wendel's Church
58 Brindle Street,
South Hampton, New York
Followed by a dinner at
Restaurant Verlane, Osgood Road 347
R.S.V.P. by the ninth of April
2. Christening invitation in Vintage style.
We need an invitation for a christening of Nico Farrowby. We would like it to be in vintage style, in light pink or lilac color and containing the photo of the baby.
It should also have some church symbols, like cross, prayer beads etc (one element is enough, not all together). Format: A5 horisontal (landscape) card. Please, find the photo attached.
Text to be included:
You are invited to
Witness and Celebrate
the Baptism of our daughter
Nico Farrowby
Sunday, September 26th at 1 p.m.
St. Ambrel Church
5821 Lindqvist Row, Parktown
Reception following the ceremony
at the Farrowby home
7302 Harlowe, Pearl Sound
Please reply by September 18th
3. Birthday invitation.
This is an invitation for Nico's 7th birthday party. The theme is racing. It should contain his photo and a race car (cars) or racing competition. No color preferences. It's a square folded card. Please, find attached the photo.
Text on the outside: Nico is turning 7
Text on the inside:
You are invited to join us
for Nico's 7th Birthday Celebration
Saturday, September 18th
We will have the celebration at Blue Juniper,
486 Quillby Road, Federal Way
Please reply by September 7th
to Bram at 175-389-602
Welcome!

```html
<!DOCTYPE html>
<html lang="en">
<head>
<meta charset="utf-8">
<title>Nico's 7th Birthday Invitation</title>
<link rel="stylesheet" href="https://fonts.googleapis.com/css2?family=Caprasimo&family=Questrial&display=swap">
<style>
  :root {
    --cream-top: #fcf7ea;
    --cream-bottom: #f8e0c3;
    --amber-light: #fbeab6;
    --amber-mid: #f6c244;
    --amber-deep: #ee8c1b;
    --title-cream: #fbe79a;
    --title-edge: rgba(176, 84, 0, 0.55);
    --accent-orange: #f2780f;
    --wine: #8a1c1c;
    --white: #ffffff;
    --seam: #fdf3dc;
    --track-haze: rgba(244, 236, 220, 0.85);
    --track-grey: #b7b3ad;
    --track-dark: #5b5754;
  }
  * { margin: 0; padding: 0; box-sizing: border-box; }
  html, body { width: 1200px; height: 1200px; overflow: hidden; background: var(--white); }
  .card {
    position: relative;
    width: 1200px;
    height: 1200px;
    font-family: "Questrial", "Century Gothic", sans-serif;
  }
  .panel { position: absolute; width: 600px; height: 600px; overflow: hidden; }
  .panel--back {
    left: 0; top: 0;
    background: linear-gradient(180deg, var(--cream-top) 0%, var(--cream-bottom) 100%);
  }
  .panel--front {
    left: 600px; top: 0;
    background:
      radial-gradient(ellipse 360px 300px at 55% 30%, rgba(255,250,225,0.95) 0%, rgba(255,240,190,0) 70%),
      linear-gradient(180deg, var(--amber-light) 0%, var(--amber-mid) 55%, var(--amber-deep) 100%);
  }
  .panel--inside-left {
    left: 0; top: 600px;
    background: linear-gradient(180deg, var(--cream-top) 0%, var(--cream-bottom) 100%);
  }
  .panel--inside-right {
    left: 600px; top: 600px;
    background: linear-gradient(180deg, var(--amber-light) 0%, var(--amber-mid) 50%, var(--amber-deep) 100%);
  }
  .seam-vertical { position: absolute; left: 599px; top: 0; width: 2px; height: 1200px; background: var(--seam); }
  .seam-horizontal { position: absolute; left: 0; top: 599px; width: 1200px; height: 2px; background: var(--seam); }

  .portrait {
    position: absolute;
    left: 112px; top: 118px;
    width: 407px; height: 299px;
    background: linear-gradient(135deg, #7da83c 0%, #a9c46a 45%, #c8d3d8 100%);
  }
  .front-title {
    position: absolute;
    left: 0; width: 600px; top: 480px;
    text-align: center;
    font-family: "Caprasimo", "Cooper Black", serif;
    font-weight: 400;
    font-size: 44px;
    line-height: 56px;
    color: var(--title-cream);
    text-shadow: 0 1px 2px var(--title-edge);
  }

  .race-scene {
    position: absolute;
    left: 37px; top: 167px;
    width: 526px; height: 357px;
    background: linear-gradient(180deg, var(--track-haze) 0%, var(--track-grey) 30%, #7c7874 65%, var(--track-dark) 100%);
  }

  .invite {
    position: absolute;
    left: 0; width: 600px; top: 0; height: 600px;
    text-align: center;
  }
  .invite__lead {
    position: absolute; left: 0; width: 100%; top: 63px;
    font-size: 25px; color: var(--wine);
  }
  .invite__name {
    position: absolute; left: 0; width: 100%; top: 138px;
    font-family: "Caprasimo", "Cooper Black", serif;
    font-weight: 400;
    font-size: 50px; color: var(--accent-orange);
    text-shadow: 0 0 6px rgba(255,255,240,0.9);
  }
  .invite__event {
    position: absolute; left: 0; width: 100%; top: 228px;
    font-size: 27px; line-height: 35px; color: var(--wine);
  }
  .invite__details {
    position: absolute; left: 0; width: 100%; top: 390px;
    font-size: 15px; line-height: 20px; color: var(--white);
  }
  .invite__welcome {
    position: absolute; left: 0; width: 100%; top: 516px;
    font-size: 30px; color: var(--white);
  }
</style>
</head>
<body>
  <main class="card">
    <section class="panel panel--back" aria-label="Back cover"></section>

    <section class="panel panel--front" aria-label="Front cover">
      <div class="portrait" role="img" aria-label="Photo of Nico smiling outdoors on grass"></div>
      <h1 class="front-title">Nico is turning 7</h1>
    </section>

    <section class="panel panel--inside-left" aria-label="Inside left">
      <div class="race-scene" role="img" aria-label="Photo of race cars rounding a track corner"></div>
    </section>

    <section class="panel panel--inside-right" aria-label="Inside right">
      <div class="invite">
        <p class="invite__lead">You are invited to join us for</p>
        <h2 class="invite__name">Nico's</h2>
        <p class="invite__event">7th Birthday Celebration<br>Saturday, September 18th</p>
        <p class="invite__details">
          We will have the celebration at Blue Juniper,<br>
          486 Quillby Road, Federal Way<br>
          Please reply by September 7th<br>
          to Bram at 175-389-602
        </p>
        <p class="invite__welcome">Welcome!</p>
      </div>
    </section>

    <div class="seam-vertical"></div>
    <div class="seam-horizontal"></div>
  </main>
</body>
</html>
```